Web Design Nutrition supplements (Quilvara 5 pages)

We are looking for templates for a new nutrition supplement shop www.velomira.ch , targeting Swiss Female 65% /Male 35% over 40 yrs with high quality products (no performance enhancement /Body building products).
Our customers are not the most proficient in internet, so the website should be simple, easily understood. not too much web2.0 look and feel and functionality.

velomira.ch product offerings are high quality and supplied from top brands: like Dr. Holtfen, Varoun, talmquist, Nobrafit), for diets, weight management, antistress, anti-apathy, oligo-elements, omega-3 oils, and cosmetics.

We want the website design
1) to reflect our seriousness and expertise in the area,
2)to Inspire trust from our customers and address their needs in a personal and professional way (we answer your questions over email/Phone)
3) though we are not an pharmacy, our products are currently sold in pharmacies in Switzerland, so we want our customers to feel as well served online, as if they were in a pharmacy.
4) compare favorably to international websites (F, G) also selling online to Swiss customers: we are a truly Swiss company and can deliver within less than 18 h. in Switzerland (so the Swiss flag is an important design element for us)

We want to provide a superior buying experience,
1) important: providing sufficient product information: (intelligible snippet/summary of product info) should be visible on search result pages, and category pages,
2) clarity of design "emphasis" on products with clear call to action (buy)

Deliverables for the winning designer;
Photoshop files that can be easily be integrated in our quilvara shop.
- Homepage
- Category Page
- Product Page
For 1st evaluation and corrections of the proposals.

- Landing Page (for SEM Campaigns)
- Newsletter (Post finch)
as a second step.

Please use the attached wireframes, that should give you the exact content we want to provide (as well as functionality), the wireframes donnot define the user experience/design (it s more like a guidance, suggestion)

Target Market(s)

Swiss Males /35% Females 65% (both Swiss French/ Swiss German over 40 years

Industry/Entity Type

Nutrition

Requirements
Must have
• Deliverables:
- Homepage
- Category Page
- Product Page

- Newsletter template
- Landing Page

We attach:
- navigation to show how users can access the products (cat/ sub cat, but also search for body parts, objectives of healing... (see Kategorien-for-web.xls)
- Wireframes (myTrevolin)
- Logo (1 psd)
- Product images (zip files)
- Benchmarks: wellmorrow.co.uk (simplicity), kpv.com (expandable navigation),
- Competitors: ro7.de, talnori.com, talnori-deutschland.de, ultra-keen.eu

```html
<!DOCTYPE html>
<html lang="de">
<head>
<meta charset="utf-8">
<title>velomira – Prä-Probiotika</title>
<link href="https://fonts.googleapis.com/css2?family=Dosis:wght@400;500;600;700&display=swap" rel="stylesheet">
<style>
:root{
  --navy:#1a2f5e;
  --navy-dark:#13244b;
  --lime:#dbe98a;
  --lime-light:#eef5b8;
  --royal:#1c45c9;
  --menu-blue:#1f48c8;
  --active-blue:#2d63e6;
  --link-blue:#4a86ff;
  --green-text:#3f9a1a;
  --orange:#e8531a;
  --badge:#8fae2c;
  --panel:#d6e4f8;
  --footer:#8fb6ee;
  --footer-link:#2c4a86;
  --body-bg:#e9e9ea;
  --white:#ffffff;
  --grey-text:#6e6e6e;
}
*{box-sizing:border-box;margin:0;padding:0}
html,body{width:1119px;height:1200px;overflow:hidden}
body{font-family:'Dosis',sans-serif;background:var(--body-bg);position:relative;color:#333}
.abs{position:absolute}

/* header */
.site-header{position:absolute;left:0;top:0;width:1119px;height:126px;background:linear-gradient(#1c3466,var(--navy-dark))}
.lang{left:134px;top:9px;font:500 13px Arial,sans-serif;color:#2c5ab0;display:flex;align-items:center;gap:8px}
.lang .flag{width:22px;height:22px;border-radius:50%;background:linear-gradient(90deg,#2140a0 33%,#fff 33% 66%,#d92323 66%)}
.lang .fr{color:#fff;text-decoration:underline}
.greeting{left:433px;top:5px;color:#fff;font-size:15px}
.greeting b{font-weight:700}
.greeting a{color:var(--link-blue);margin-left:10px}
.account{left:904px;top:5px;color:var(--link-blue);font-size:15px;text-decoration:underline}
.logo{left:85px;top:58px;display:flex;align-items:center;gap:6px}
.logo .mark{width:28px;height:28px;border:3px solid #7bbf2e;border-radius:6px}
.logo span{font:500 31px 'Dosis',sans-serif;color:#8aa0b8;letter-spacing:.5px}
.perk{display:flex;align-items:center;gap:6px;color:#fff;font:600 12px/14px Arial,sans-serif;top:50px;white-space:nowrap}
.perk svg{flex:none}
.search{left:390px;top:91px;width:327px;height:29px;display:flex}
.search .field{flex:1;background:linear-gradient(#fff,#dfe3ea)}
.search .btn{width:27px;background:#2ea83a;display:flex;align-items:center;justify-content:center}
.cart{left:839px;top:51px;width:108px;height:39px;border:2px solid #fff;border-radius:4px;background:var(--menu-blue);color:#fff;font:500 13.5px/16px Arial,sans-serif;padding:2px 4px;white-space:nowrap;overflow:hidden}
.bag{left:970px;top:35px}
.help{left:969px;top:104px;color:var(--link-blue);font-size:13px;display:flex;align-items:center;gap:5px;text-decoration:underline}
.help i{font-style:normal;width:18px;height:18px;border:2px solid var(--link-blue);border-radius:50%;display:flex;align-items:center;justify-content:center;font-size:12px;font-weight:700;text-decoration:none}

/* nav */
.main-nav{position:absolute;left:0;top:126px;width:1119px;height:48px;background:linear-gradient(var(--lime-light),var(--lime));display:flex;padding-left:83px}
.main-nav a{font-size:16px;color:#3b3b3b;padding:0 5px;line-height:48px;border-right:1px solid #fff;text-decoration:none;white-space:nowrap}
.main-nav a:last-child{border:none}
.main-nav a.active{background:var(--active-blue);color:#fff}

/* content area */
.content{position:absolute;left:83px;top:174px;width:939px;height:784px;background:var(--panel)}
.box{position:absolute;background:#fff;border-radius:8px;box-shadow:0 2px 4px rgba(0,0,0,.15)}
.side-menu{left:83px;top:189px;width:185px;height:190px}
.side-menu ul{position:absolute;left:7px;top:8px;width:170px;height:173px;background:linear-gradient(var(--navy),var(--menu-blue));list-style:none;padding-top:4px}
.side-menu li{color:#fff;font-size:12px;height:24.8px;line-height:24.8px;padding-left:18px;white-space:nowrap}
.side-menu li.active{background:var(--active-blue);margin-left:-5px;margin-right:-7px;padding-left:23px;font-weight:700}
.hero{left:277px;top:189px;width:552px;height:188px}
.hero .inner{position:absolute;left:8px;top:6px;width:537px;height:175px;background:linear-gradient(100deg,#17a83a 0%,#0b9440 55%,#1758d0 100%);color:#fff;padding:12px 25px;overflow:hidden}
.hero h1{font-size:36px;font-weight:700;line-height:34px}
.hero h2{font-size:17px;font-weight:700;line-height:18px}
.hero p{font-size:14px;line-height:17px;margin-top:10px;width:215px}
.hero .pack{position:absolute;right:10px;top:12px;width:278px;height:163px;background:linear-gradient(90deg,#dfe7f3 0%,#ffffff 35%,#e8eef8 50%,#ffffff 70%,#cfdcf0 100%)}
.callcentre{left:836px;top:189px;width:185px;height:188px}
.callcentre .inner{position:absolute;left:8px;top:6px;width:169px;height:175px;background:linear-gradient(90deg,#dfe8f7,#f6f8fc);padding:18px 0 0 22px;color:var(--royal);font-weight:700}
.callcentre .big{font-size:17px;line-height:20px}
.callcentre .small{font-size:12px;line-height:15px;margin-top:10px}
.callcentre .photo{position:absolute;right:6px;top:16px;width:62px;height:159px;background:linear-gradient(#e9ecf2,#d4dae6);border-radius:30px 30px 0 0}

.features{left:83px;top:389px;width:939px;height:211px}
.feature{position:absolute;top:40px;width:300px;height:160px}
.feature h3{font-size:26px;font-weight:700;color:var(--royal);line-height:24px}
.feature h4{font-size:21px;font-weight:400;color:var(--royal);line-height:22px}
.feature p{font-size:13.5px;color:var(--green-text);line-height:17px;margin-top:7px;width:140px}
.feature .more{position:absolute;left:64px;top:138px;color:var(--green-text);font-size:14px;display:flex;align-items:center;gap:6px}
.feature .pack{position:absolute;left:168px;top:-12px;width:115px;height:160px;background:linear-gradient(90deg,#eeeeee,#ffffff 45%,#dedede);border-top:10px solid #f0a33a;border-radius:2px}

.card{position:absolute;top:608px;width:184px;height:327px}
.card h5{position:absolute;left:13px;top:17px;font-size:17px;font-weight:500;color:var(--royal);white-space:nowrap}
.card .desc{position:absolute;left:13px;top:38px;width:150px;font-size:11px;line-height:14px;color:var(--grey-text)}
.card .bottle{position:absolute;left:50px;top:76px;width:78px;height:143px;background:linear-gradient(90deg,#1c2f5e,#3a5aa0 45%,#1a2d5a);border-radius:8px 8px 14px 14px}
.card .badge{position:absolute;left:112px;top:68px;width:54px;height:54px;border-radius:50%;background:var(--badge);color:#fff;text-align:center;font-weight:700;font-size:22px;line-height:22px;padding-top:9px}
.card .badge small{display:block;font-size:8px;line-height:8px;font-weight:500}
.card hr{position:absolute;left:8px;right:8px;top:236px;border:none;border-top:1px solid #e2e2e2}
.card .old{position:absolute;left:0;right:0;top:240px;text-align:center;font-size:13px;color:#555;text-decoration:line-through}
.card .price{position:absolute;left:0;right:0;top:256px;text-align:center;font-size:16px;color:var(--orange)}
.card .view{position:absolute;left:62px;top:283px;width:60px;height:23px;background:linear-gradient(#f26a22,#d8460e);color:#fff;font-size:13px;text-align:center;line-height:23px}

/* footer */
.site-footer{position:absolute;left:0;top:958px;width:1119px;height:242px;background:linear-gradient(var(--footer),#a5c5f3)}
.site-footer a{color:var(--footer-link);text-decoration:underline;font-size:13px}
.legal{position:absolute;left:101px;top:20px;font-size:14px;color:var(--footer-link)}
.legal a{font-size:14px;margin:0 6px}
.legal a:first-child{margin-left:0}
.fcol{position:absolute;top:56px;display:flex;flex-direction:column;gap:9.5px}
.social{position:absolute;top:192px;width:24px;height:24px;border-radius:4px}
</style>
</head>
<body>

<header class="site-header">
  <div class="abs lang"><span>DE</span><span class="flag"></span><span class="fr">FR</span></div>
  <div class="abs greeting">Hallo <b>Leonie</b><a href="#">(Sind Sie nicht Leonie?)</a></div>
  <a class="abs account" href="#">Mein Konto</a>
  <div class="abs logo"><span class="mark"></span><span>velomira</span></div>

  <div class="abs perk" style="left:342px">
    <svg width="30" height="30" viewBox="0 0 30 30"><circle cx="15" cy="15" r="13" fill="none" stroke="#2b6ad6" stroke-width="2"/><path d="M15 7v8h6" stroke="#2b6ad6" stroke-width="2" fill="none"/></svg>
    <span>18 Std. Lieferung<br>in der Schweiz</span>
  </div>
  <div class="abs perk" style="left:484px">
    <svg width="28" height="28" viewBox="0 0 28 28"><circle cx="14" cy="14" r="12" fill="none" stroke="#2b6ad6" stroke-width="2"/><text x="14" y="17" font-size="8" fill="#2b6ad6" text-anchor="middle" font-family="Arial">CHF</text></svg>
    <span>Gratisversand<br>ab 80 CHF</span>
  </div>
  <div class="abs perk" style="left:607px">
    <svg width="30" height="28" viewBox="0 0 30 28"><rect x="2" y="4" width="7" height="20" fill="none" stroke="#2b6ad6" stroke-width="2"/><rect x="11" y="4" width="7" height="20" fill="none" stroke="#2b6ad6" stroke-width="2"/><rect x="20" y="4" width="7" height="20" fill="none" stroke="#2b6ad6" stroke-width="2"/></svg>
    <span>Experten Beratung</span>
  </div>

  <div class="abs search"><div class="field"></div><div class="btn"><svg width="16" height="16" viewBox="0 0 16 16"><circle cx="7" cy="7" r="5" fill="none" stroke="#fff" stroke-width="2.2"/><path d="M11 11l4 4" stroke="#fff" stroke-width="2.4"/></svg></div></div>
  <div class="abs cart">Zum Warenkorb<br>12,90 CHF</div>
  <svg class="abs bag" width="46" height="64" viewBox="0 0 46 64"><path d="M4 10h38l3 54H1z" fill="#3bc23a"/><path d="M16 12v-6a7 7 0 0 1 14 0v6" fill="none" stroke="#fff" stroke-width="2.5"/><text x="23" y="46" font-size="13" font-family="Arial" font-weight="700" text-anchor="middle" fill="#163">1</text></svg>
  <div class="abs help">hilfe <i>?</i></div>
</header>

<nav class="main-nav">
  <a href="#">Vitamins</a><a href="#">Mineralien</a><a href="#">Essentielle Fettsäure</a><a href="#" class="active">Prä-Probiotika</a><a href="#">Spirulina-Maca</a><a href="#">Gewichtsabnahme</a><a href="#">Kosmetik</a><a href="#">Phytotherapie</a><a href="#">funktionelle Nahrung</a><a href="#">ANGEBOTE</a>
</nav>

<main>
  <div class="content"></div>

  <div class="box side-menu">
    <ul>
      <li>Präbiotika</li><li>Probiotika</li><li>Isemolorum</li><li class="active">Ipsemlorum amet sit dol</li><li>...</li><li>lorem ipsum</li><li>lorem ipsum</li>
    </ul>
  </div>

  <div class="box hero">
    <div class="inner">
      <h1>LOREM IPSUM</h1>
      <h2>Dolor sit amet</h2>
      <p>This is Photoshop's version of Lorem Ipsum. Proin gravida nibh vel velit auctor aliquet. Aenean sollicitudin, lorem quis bibendum auctor, nisi elit consequat ipsum, nec sagittis sem</p>
      <div class="pack" role="img" aria-label="Zwei Produktpackungen nebeneinander"></div>
    </div>
  </div>

  <div class="box callcentre">
    <div class="inner">
      <div class="big">Customer<br>call<br>centre</div>
      <div class="small">Customer<br>call<br>centre</div>
      <div class="small" style="margin-top:4px">987 654</div>
      <div class="photo" role="img" aria-label="Foto einer Kundenberaterin mit Headset"></div>
    </div>
  </div>

  <div class="box features">
    <div class="feature" style="left:30px">
      <h3>LOREM IPSUM</h3><h4>dolor sit amet</h4>
      <p>Aenean sollicitudin, lorem quis bibendum auctor, nisi elit consequat ipsum, nec sagittis sem</p>
      <div class="pack" role="img" aria-label="Produktpackung mit Siegel"></div>
      <div class="more">read more <svg width="14" height="14"><path d="M1 1l12 6-12 6z" fill="#f5b41e"/></svg></div>
    </div>
    <div class="feature" style="left:339px">
      <h3>LOREM IPSUM</h3><h4>dolor sit amet</h4>
      <p>Aenean sollicitudin, lorem quis bibendum auctor, nisi elit consequat ipsum, nec sagittis sem</p>
      <div class="pack" role="img" aria-label="Produktpackung mit Preisstempel"></div>
      <div class="more">read more <svg width="14" height="14"><path d="M1 1l12 6-12 6z" fill="#f5b41e"/></svg></div>
    </div>
    <div class="feature" style="left:650px">
      <h3>LOREM IPSUM</h3><h4>dolor sit amet</h4>
      <p>Aenean sollicitudin, lorem quis bibendum auctor, nisi elit consequat ipsum, nec sagittis sem</p>
      <div class="pack" role="img" aria-label="Produktpackung"></div>
      <div class="more">read more <svg width="14" height="14"><path d="M1 1l12 6-12 6z" fill="#f5b41e"/></svg></div>
    </div>
  </div>

  <div class="box card" style="left:83px"><h5>LOREM IPSUM DOLOR</h5><div class="desc">Sit amet dosis magma kurulet dolor amet sit</div><div class="bottle" role="img" aria-label="Produktdose Basentabletten"></div><div class="badge">10%<small>OFF</small></div><hr><div class="old">38,50 SFR</div><div class="price">35,00 SFR</div><div class="view">view</div></div>
  <div class="box card" style="left:271px"><h5>LOREM IPSUM DOLOR</h5><div class="desc">Sit amet dosis magma kurulet dolor amet sit</div><div class="bottle" role="img" aria-label="Produktdose Basentabletten"></div><div class="badge">10%<small>OFF</small></div><hr><div class="old">38,50 SFR</div><div class="price">35,00 SFR</div><div class="view">view</div></div>
  <div class="box card" style="left:459px"><h5>LOREM IPSUM DOLOR</h5><div class="desc">Sit amet dosis magma kurulet dolor amet sit</div><div class="bottle" role="img" aria-label="Produktdose Basentabletten"></div><div class="badge">10%<small>OFF</small></div><hr><div class="old">38,50 SFR</div><div class="price">35,00 SFR</div><div class="view">view</div></div>
  <div class="box card" style="left:647px"><h5>LOREM IPSUM DOLOR</h5><div class="desc">Sit amet dosis magma kurulet dolor amet sit</div><div class="bottle" role="img" aria-label="Produktdose Basentabletten"></div><div class="badge">10%<small>OFF</small></div><hr><div class="old">38,50 SFR</div><div class="price">35,00 SFR</div><div class="view">view</div></div>
  <div class="box card" style="left:835px"><h5>LOREM IPSUM DOLOR</h5><div class="desc">Sit amet dosis magma kurulet dolor amet sit</div><div class="bottle" role="img" aria-label="Produktdose Basentabletten"></div><div class="badge">10%<small>OFF</small></div><hr><div class="old">38,50 SFR</div><div class="price">35,00 SFR</div><div class="view">view</div></div>
</main>

<footer class="site-footer">
  <div class="legal"><a href="#">Impressum</a> | <a href="#">Wer sind Wir?</a> | <a href="#">Über uns</a> | <a href="#">AGB's</a></div>
  <div class="fcol" style="left:102px"><a href="#">KUNDENSERVICE</a><a href="#">Kontakt</a><a href="#">Lexikon Hilfe &amp; Antworten</a><a href="#">Blog</a><a href="#">Partnerprogramm</a><a href="#">Reseller Program</a></div>
  <div class="fcol" style="left:269px"><a href="#">NAVIGATIONSHILFE</a><a href="#">Suchbegriffe</a><a href="#">Marken</a><a href="#">Erweiterte Suche</a><a href="#">Sitemap</a></div>
  <div class="fcol" style="left:423px"><a href="#">Das Unternehmen</a><a href="#">Expertise</a><a href="#">Jobs</a><a href="#">User Team</a></div>
  <div class="social" style="left:907px;background:#3a5ea8" role="img" aria-label="Soziales Netzwerk"></div>
  <div class="social" style="left:940px;background:#4aa6e0" role="img" aria-label="Soziales Netzwerk"></div>
</footer>

</body>
</html>
```